RTamberly Business Cards & Letterhead

I have a logo but need a design for some new business cards. We are a Design-Build Firm that specializes in the design and construction of commercial projects.
the cards need to be professional. no cartoon stuff.
i would like to have the cards in AI format so I can update the card as needed. Logo is provided.
Our Address is: 4183 Marwood Ln. Larkdale, West Oregon 27614

```html
<!DOCTYPE html>
<html lang="en">
<head>
<meta charset="UTF-8">
<title>RTamberly Business Card</title>
<link href="https://fonts.googleapis.com/css2?family=Open+Sans:wght@400;600;700&display=swap" rel="stylesheet">
<style>
  :root {
    --stage: #2b2b2b;
    --card-dark: #454545;
    --card-light: #ffffff;
    --ink: #3a3a3a;
    --ink-soft: #4a4a4a;
    --accent: #1b6fb5;
    --silver: #b9b9b9;
    --rule: #8a8a8a;
  }
  * { margin: 0; padding: 0; box-sizing: border-box; }
  html, body { width: 1200px; height: 875px; overflow: hidden; }
  body {
    background: var(--stage);
    font-family: "Open Sans", sans-serif;
    position: relative;
  }
  .card {
    position: absolute;
    left: 320px;
    width: 560px;
    height: 320px;
    border-radius: 22px;
    overflow: hidden;
  }
  .card--front { top: 95px; background: var(--card-dark); }
  .card--back { top: 460px; background: var(--card-light); }

  .wordmark {
    display: flex;
    align-items: center;
    gap: 12px;
    font-weight: 700;
    letter-spacing: 1px;
    line-height: 1;
    white-space: nowrap;
  }
  .wordmark__square { display: block; flex: none; }
  .card--front .wordmark {
    position: absolute;
    left: 50%; top: 50%;
    transform: translate(-50%, -50%);
    font-size: 62px;
    color: var(--silver);
  }
  .card--front .wordmark__square { width: 44px; height: 44px; background: var(--silver); }

  .card--back .wordmark {
    position: absolute;
    right: 40px; top: 46px;
    font-size: 32px;
    color: var(--ink);
    gap: 8px;
  }
  .card--back .wordmark__square { width: 22px; height: 22px; background: var(--accent); }

  .person {
    position: absolute;
    left: 36px; top: 122px;
  }
  .person__name {
    font-size: 25px;
    font-weight: 700;
    color: var(--ink);
    line-height: 1.1;
  }
  .person__title {
    font-size: 16px;
    color: var(--accent);
    line-height: 1.3;
  }
  .rule {
    position: absolute;
    left: 30px; right: 30px; top: 180px;
    height: 1px;
    background: var(--rule);
  }
  .contacts {
    position: absolute;
    left: 42px; top: 192px;
    list-style: none;
    font-size: 14px;
    color: var(--ink-soft);
  }
  .contacts li {
    display: flex;
    align-items: center;
    gap: 10px;
    height: 22px;
    white-space: nowrap;
  }
  .contacts svg { width: 13px; height: 13px; fill: var(--accent); flex: none; }
  .company {
    position: absolute;
    right: 36px; top: 192px;
    text-align: right;
    font-size: 14px;
    line-height: 22px;
    color: var(--ink-soft);
    white-space: nowrap;
  }
  .company__name { color: var(--accent); font-weight: 600; }
</style>
</head>
<body>

  <section class="card card--front">
    <div class="wordmark"><span class="wordmark__square"></span>RTAMBERLY</div>
  </section>

  <section class="card card--back">
    <div class="wordmark"><span class="wordmark__square"></span>RTAMBERLY</div>

    <div class="person">
      <p class="person__name">DANIEL HARROW</p>
      <p class="person__title">Founder &amp; CEO</p>
    </div>

    <div class="rule"></div>

    <ul class="contacts">
      <li>
        <svg viewBox="0 0 16 16"><path d="M3.5 1.5l2.5 0 1.2 3.2-1.6 1.1c.8 1.8 2.2 3.2 4 4l1.1-1.6 3.3 1.2v2.5c0 .9-.8 1.6-1.7 1.5C6.9 13 3 9.1 2 3.2 1.9 2.3 2.6 1.5 3.5 1.5z"/></svg>
        (555) 210-4477
      </li>
      <li>
        <svg viewBox="0 0 16 16"><path d="M4.5 1h7c.6 0 1 .4 1 1v12c0 .6-.4 1-1 1h-7c-.6 0-1-.4-1-1V2c0-.6.4-1 1-1zm.7 2v9h5.6V3H5.2zM8 12.6a.7.7 0 100 1.4.7.7 0 000-1.4z"/></svg>
        (555) 318-6620
      </li>
      <li>
        <svg viewBox="0 0 16 16"><path d="M4 1h6l2 2v3H4V1zM2 7h12c.6 0 1 .4 1 1v4h-3v3H4v-3H1V8c0-.6.4-1 1-1zm3.5 4.5v2h5v-2h-5z"/></svg>
        (555) 318-6621
      </li>
      <li>
        <svg viewBox="0 0 16 16"><path d="M1 3h14v10H1V3zm1.6 1.3L8 8.4l5.4-4.1H2.6z"/></svg>
        office@rtamberly.example
      </li>
    </ul>

    <div class="company">
      <p class="company__name">RTAMBERLY INC</p>
      <p>4183 Marwood Ln. Larkdale</p>
      <p>West Oregon 27614</p>
      <p>www.rtamberly.example</p>
    </div>
  </section>

</body>
</html>
```